New homepage and Product page - Meadow Vy

Reason: I have narrowed it done to 3 designers and just need to get the designs revised

Industry/Entity Type

Product

```html
<!DOCTYPE html>
<html lang="en">
<head>
<meta charset="utf-8">
<title>Meadow Vy — Home</title>
<link href="https://fonts.googleapis.com/css2?family=Nunito+Sans:wght@300;400;600;700&display=swap" rel="stylesheet">
<style>
:root{
  --green-dark:#4a9a0a;
  --green:#5cae0c;
  --green-light:#7cc41e;
  --heading-green:#4f7f25;
  --text-grey:#5f5f5f;
  --footer-bg:#ecebe7;
  --orange:#ee7f22;
  --coffee:#2a8c46;
  --berry:#d81f2a;
  --link:#6aab0a;
  --rule:#c9c8c4;
  --icon:#8a8a8a;
}
*{margin:0;padding:0;box-sizing:border-box}
html,body{width:1200px;height:1000px;overflow:hidden}
body{font-family:"Nunito Sans",Arial,sans-serif;background:var(--footer-bg);position:relative;color:var(--text-grey)}
.hero{position:absolute;left:0;top:0;width:1200px;height:210px;
  background:linear-gradient(180deg,var(--green-light) 0%,var(--green) 60%,var(--green-dark) 100%);overflow:hidden}
.hero-copy{position:absolute;left:120px;top:-22px;width:460px;color:#fff;font-weight:600;font-size:17px;line-height:26px}
.btn-learn{position:absolute;left:120px;top:73px;width:176px;height:50px;background:var(--orange);
  border:3px solid #fff;border-radius:4px;color:#fff;font-size:19px;font-weight:400;
  display:flex;align-items:center;padding-left:15px;text-decoration:none;letter-spacing:.3px}
.btn-learn span{margin-left:12px;color:#ffd39c;font-weight:700}
.tagline-art{position:absolute;left:312px;top:66px;width:346px;height:52px;border-radius:6px;
  background:linear-gradient(90deg,rgba(220,245,150,.35),rgba(220,245,150,.2))}
.hero-product{position:absolute;left:766px;top:-10px;width:284px;height:220px;border-radius:4px;
  background:linear-gradient(180deg,#f3f3ef 0%,#f6a63b 30%,#e68a1e 55%,#f3f3ef 70%,#e8e8e4 100%)}
.hero-tab{position:absolute;left:500px;top:190px}
.main{position:absolute;left:0;top:210px;width:1200px;height:450px;background:#fff}
.title{position:absolute;left:0;top:246px;width:1200px;text-align:center;font-weight:300;font-size:44px;
  color:var(--heading-green);letter-spacing:.5px;text-transform:uppercase}
.intro{position:absolute;left:180px;top:301px;width:840px;text-align:center;font-size:21px;line-height:30px;font-weight:400;color:var(--text-grey)}
.card{position:absolute;top:400px;width:300px;height:340px;background:#fff;box-shadow:0 6px 6px -4px rgba(0,0,0,.18)}
.card h2{height:40px;color:#fff;font-weight:400;font-size:21px;text-align:center;line-height:40px;text-transform:uppercase;letter-spacing:.3px}
.card .shot{position:absolute;left:0;top:42px;width:300px;height:298px;background:linear-gradient(180deg,#dcdcd6 0%,#f4f4f1 60%,#fff 100%)}
.card .pack{position:absolute;left:66px;top:42px;width:170px;height:218px;border-radius:2px}
.card-garcinia{left:120px}.card-garcinia h2{background:var(--orange)}
.card-garcinia .pack{background:linear-gradient(180deg,#fafafa 0%,#f7f7f5 25%,#ee7f22 38%,#f5c61c 48%,#e48a22 65%,#fafafa 100%)}
.card-coffee{left:450px}.card-coffee h2{background:var(--coffee)}
.card-coffee .pack{background:linear-gradient(180deg,#fafafa 0%,#f7f7f5 25%,#1e8a44 38%,#f5c61c 48%,#5f9a3a 65%,#fafafa 100%)}
.card-berry{left:780px}.card-berry h2{background:var(--berry)}
.card-berry .pack{background:linear-gradient(180deg,#fafafa 0%,#f7f7f5 25%,#d81f2a 38%,#f5c61c 48%,#b81f2e 65%,#fafafa 100%)}
.rule{position:absolute;left:120px;width:960px;height:1px;background:var(--rule)}
.badge{position:absolute;left:119px;top:797px}
.about{position:absolute;left:206px;top:802px;width:540px;font-size:14px;line-height:20px;color:var(--text-grey)}
.about a{color:var(--link);font-weight:600;text-decoration:none}
.foot-nav{position:absolute;right:119px;top:802px;font-size:13px;color:var(--link)}
.foot-nav a{color:var(--link);text-decoration:none}
.foot-nav .sep{margin:0 6px;color:#999}
.social{position:absolute;left:970px;top:831px;display:flex;gap:10px}
.social span{display:block;width:30px;height:30px;background:var(--icon);border-radius:2px}
.copyright{position:absolute;left:120px;top:903px;font-size:12px;color:#777}
.credit{position:absolute;right:118px;top:903px;font-size:12px;color:#777}
.credit b{color:#555;font-weight:700}
</style>
</head>
<body>
<header class="hero">
  <p class="hero-copy">Meadow Vy garcinia cambogia that supplies 60% HCA, which is the active weight-loss component of garcinia cambogia.</p>
  <a class="btn-learn" href="#">LEARN MORE <span>❯</span></a>
  <div class="tagline-art" role="img" aria-label="Hand-lettered slogan: Start Losing Weight Today!"></div>
  <div class="hero-product" role="img" aria-label="Garcinia cambogia two-bottle bonus pack with leaves"></div>
  <svg class="hero-tab" width="200" height="20" viewBox="0 0 200 20" aria-hidden="true">
    <path d="M0 20 C30 20 30 4 60 4 L140 4 C170 4 170 20 200 20 Z" fill="#fff"/>
    <rect x="73" y="13" width="14" height="5" rx="2.5" fill="#5aa41a"/>
    <rect x="93" y="13" width="14" height="5" rx="2.5" fill="#dcdcd8"/>
    <rect x="113" y="13" width="14" height="5" rx="2.5" fill="#dcdcd8"/>
  </svg>
</header>

<section class="main"></section>
<h1 class="title">The Best of Nature &amp; Science</h1>
<p class="intro">New Meadow Vy is line of natural, high-quality, weight-loss supplements that are scientifically formulated for better efficiency!</p>

<article class="card card-garcinia">
  <h2>Garcinia Cambogia</h2>
  <div class="shot"><div class="pack" role="img" aria-label="Garcinia cambogia supplement box with green leaves"></div></div>
</article>
<article class="card card-coffee">
  <h2>Green Coffee Bean</h2>
  <div class="shot"><div class="pack" role="img" aria-label="Green coffee bean supplement box with green leaves"></div></div>
</article>
<article class="card card-berry">
  <h2>Rasberry Ketone</h2>
  <div class="shot"><div class="pack" role="img" aria-label="Raspberry ketone supplement box with green leaves"></div></div>
</article>

<footer>
  <div class="rule" style="top:777px"></div>
  <svg class="badge" width="70" height="70" viewBox="0 0 70 70" aria-hidden="true"><circle cx="35" cy="35" r="34" fill="#6b625a"/></svg>
  <p class="about">Lorem ipsum dolor sit amet, consectetur adipisicing elit, sed do eiusmod incididunt ut labore et dolore magna aliqua enim ad minim veniam, quis nostrud exercitation ullamco laboris nisi ut aliquip ex ea commodo consequat ... <a href="#">Find out more</a></p>
  <nav class="foot-nav"><a href="#">Home</a><span class="sep">|</span><a href="#">Products</a><span class="sep">|</span><a href="#">Contact Us</a></nav>
  <div class="social"><span aria-label="Social link 1"></span><span aria-label="Social link 2"></span><span aria-label="Social link 3"></span></div>
  <div class="rule" style="top:887px"></div>
  <p class="copyright">© Copyright 2014 Lindqvist Studio</p>
  <p class="credit">Website by <b>Lindqvist Studio</b></p>
</footer>
</body>
</html>
```